Detail Shop Business card design

i need a business card design for my new detailing company called 'Brenner's Detail Shop'. i want an all black and white design . simple, direct and to the point. i want the designer to choose a fitting font to match the logothe front should have logo, address, phone and email and the back side should have a slogan and text indicating that we offer services on anything including cars, trucks, motorcycles and RVs. slogan will read "we take pride in your ride"
maybe also very small on the back side the IG icon with Brenners_Detail_Shop

phone 482.615.7734
address 7384 E Harlow Ave
Spokane WA 99342
email: BrennersDetail@quorvail.com

Target Market(s)

all ages , auto enthusiasts

Industry/Entity Type

Automotive

Contact Information for Business Card

the front should have logo, address, phone and email and the back side should have a slogan and text indicating that we offer services on anything including cars, trucks, motorcycles and RVs. slogan will read "we take pride in your ride"

phone 482.615.7734
address 7384 E Harlow Ave
Spokane WA 99342

Colors
000000
ffffff

Requirements
Must have
• bold font and very simple design with good spacing
Nice to have
• anything creative from the designer indicating we service any types of vehicles
Should not have
• any colors ,

```html
<!DOCTYPE html>
<html lang="en">
<head>
<meta charset="utf-8">
<title>Brenner's Detail Shop – Business Card</title>
<link rel="stylesheet" href="https://fonts.googleapis.com/css2?family=Lato:wght@400;700;900&display=swap">
<style>
  :root {
    --ink: #000000;
    --paper: #ffffff;
    --backdrop: #e4e4e4;
    --ghost: #ececec;
    --ghost-edge: #f6f6f6;
  }
  * { box-sizing: border-box; margin: 0; padding: 0; }
  html, body { width: 1200px; height: 800px; overflow: hidden; }
  body {
    background: var(--backdrop);
    font-family: "Lato", Arial, sans-serif;
    color: var(--ink);
    display: flex;
    align-items: center;
    justify-content: center;
    gap: 60px;
  }
  .card {
    position: relative;
    width: 520px;
    height: 297px;
    background: var(--paper);
    box-shadow: 0 2px 10px rgba(0,0,0,0.12);
  }
  .card-frame {
    position: absolute;
    inset: 14px;
    border: 2px solid var(--ink);
  }
  /* contact side */
  .vehicle-art {
    position: absolute;
    left: 40px;
    top: 70px;
    width: 400px;
    height: 160px;
    border-radius: 60px 90px 40px 40px;
    background: radial-gradient(ellipse at 50% 55%, var(--ghost) 0%, var(--ghost) 55%, var(--ghost-edge) 100%);
  }
  .contact {
    position: absolute;
    inset: 0;
    display: flex;
    flex-direction: column;
    align-items: center;
    justify-content: center;
    text-align: center;
    padding-left: 40px;
  }
  .contact-name { font-weight: 900; font-size: 17px; letter-spacing: 0.2px; }
  .contact-role { font-size: 12px; margin-bottom: 6px; }
  .contact-line { font-size: 13px; font-weight: 700; line-height: 1.35; }
  .slogan {
    margin-top: 6px;
    font-size: 14px;
    letter-spacing: 7px;
  }
  /* brand side */
  .brand {
    position: absolute;
    inset: 0;
    display: flex;
    flex-direction: column;
    align-items: center;
    justify-content: center;
    text-align: center;
  }
  .brand-mark {
    display: flex;
    align-items: center;
    gap: 10px;
    margin-bottom: 14px;
  }
  .brand-dot {
    width: 26px;
    height: 26px;
    border-radius: 50%;
    background: var(--ink);
  }
  .brand-name { font-weight: 900; font-size: 24px; }
  .services-title { font-weight: 900; font-size: 14px; }
  .services-list { font-size: 12px; letter-spacing: 0.4px; margin-top: 2px; }
</style>
</head>
<body>
  <section class="card card-contact">
    <div class="card-frame"></div>
    <div class="vehicle-art" role="img" aria-label="Faint grey illustration of a classic hot rod behind the contact details"></div>
    <div class="contact">
      <p class="contact-name">DALE MORROW</p>
      <p class="contact-role">Owner</p>
      <p class="contact-line">P: 482.615.7734 | E: BrennersDetail@quorvail.com</p>
      <p class="contact-line">7384 E Harlow Ave, Spokane WA 99342</p>
      <p class="slogan">we take pride in your ride</p>
    </div>
  </section>

  <section class="card card-brand">
    <div class="card-frame"></div>
    <div class="brand">
      <div class="brand-mark">
        <span class="brand-dot"></span>
        <span class="brand-name">Brenner's Detail Shop</span>
      </div>
      <p class="services-title">we offer services</p>
      <p class="services-list">cars | trucks | motorcycle | boats and rvs</p>
    </div>
  </section>
</body>
</html>
```